Storm Restoration Contractor needs a professional business card design

Looking for a professional business card design. Not looking for your cheapo MS Word standard ones that are readily available. Dont want it to be cookie cutter look like ones readily available online. We just recently changed our logo and want to freshen up all our documents. Our company handles restoring a property back to a pre-loss condition after a storm damages it. For example, wind, hail, flood, fire losses.

Target Market(s)

Property Owners, Homeowners, Property Owners, Commercial Property Owners, Property Management Companies, Hail and Wind Damaged Properties

Industry/Entity Type

Construction Company

Contact Information for Business Card

Bramwell Outworks
555-418-7302
555-418-9047 fax
www.bramwelloutworks.example
info@bramwelloutworks.example

Requirements
Must have
• Clean, Professional, fresh look
• Storm Restoration, Roofing, Siding, Windows
Nice to have
• If there is a way to incorporate storms that may be cool.

```html
<!DOCTYPE html>
<html lang="en">
<head>
<meta charset="utf-8">
<title>Bramwell Outworks – Business Card</title>
<link rel="stylesheet" href="https://fonts.googleapis.com/css2?family=Montserrat:wght@400;500;700&display=swap">
<style>
  :root {
    --brand-blue: #1477c4;
    --ink-grey: #555a60;
    --strip-grey: #5d6166;
    --rule-grey: #9a9ea3;
    --faint-blue: #e3eef8;
    --card-white: #ffffff;
    --page-bg: #e9eaec;
  }
  * { margin: 0; padding: 0; box-sizing: border-box; }
  html, body { width: 1200px; height: 900px; overflow: hidden; }
  body {
    background: var(--page-bg);
    font-family: "Montserrat", sans-serif;
    position: relative;
  }
  .card {
    position: absolute;
    width: 600px;
    height: 343px;
    border-radius: 18px;
    overflow: hidden;
    box-shadow: 0 10px 28px rgba(0,0,0,0.18);
  }

  /* Back side */
  .card-back {
    left: 70px; top: 80px;
    background: var(--brand-blue);
    color: var(--card-white);
  }
  .back-mark {
    position: absolute;
    left: 0; right: 0; top: 112px;
    display: flex; align-items: center; justify-content: center; gap: 18px;
  }
  .back-mark .mark-circle {
    width: 64px; height: 64px;
    border: 9px solid var(--card-white);
    border-radius: 50%;
  }
  .back-mark .mark-name {
    font-weight: 700; font-size: 30px; letter-spacing: 0.5px;
  }
  .back-url {
    position: absolute; left: 0; right: 0; bottom: 34px;
    text-align: center; font-size: 15px; font-weight: 500; letter-spacing: 0.3px;
  }

  /* Front side */
  .card-front {
    left: 530px; top: 470px;
    background: var(--card-white);
  }
  .front-edges { position: absolute; inset: 0; }
  .faint-ring {
    position: absolute; left: 300px; top: 20px;
    width: 300px; height: 300px;
    border: 30px solid var(--faint-blue);
    border-radius: 50%;
  }
  .brand-lockup {
    position: absolute; left: 44px; top: 62px;
    display: flex; align-items: center;
  }
  .brand-lockup .mark-circle {
    width: 50px; height: 50px;
    border: 6px solid var(--brand-blue);
    border-radius: 50%;
  }
  .brand-lockup .divider {
    width: 2px; height: 78px; background: var(--brand-blue);
    margin: 0 14px;
  }
  .brand-lockup .mark-name {
    font-weight: 700; font-size: 25px; line-height: 1.05;
    color: var(--brand-blue); text-transform: uppercase; letter-spacing: 0.5px;
  }
  .top-rule {
    position: absolute; left: 130px; right: 40px; top: 142px;
    height: 1px; background: var(--rule-grey);
  }
  .services {
    position: absolute; right: 24px; top: 156px;
    list-style: none; text-align: right;
    font-size: 14px; line-height: 19px; color: var(--ink-grey);
  }
  .services li::after {
    content: ""; display: inline-block;
    width: 6px; height: 6px; border-radius: 50%;
    background: var(--brand-blue); margin-left: 8px; vertical-align: middle;
  }
  .person {
    position: absolute; left: 62px; top: 190px; width: 280px;
  }
  .person-name {
    font-weight: 700; font-size: 22px; color: var(--brand-blue);
  }
  .person-title {
    display: flex; align-items: center; gap: 8px;
    font-size: 13px; color: var(--ink-grey);
  }
  .person-title::after {
    content: ""; flex: 1; height: 1px; background: var(--rule-grey);
  }
  .contacts {
    position: absolute; left: 62px; top: 250px;
    list-style: none; font-size: 14.5px; color: var(--ink-grey);
  }
  .contacts li {
    display: flex; align-items: center; gap: 10px; height: 20px;
  }
  .contacts svg { width: 12px; height: 12px; fill: var(--brand-blue); flex: none; }
  .contacts .url-accent { color: var(--brand-blue); font-weight: 700; }
</style>
</head>
<body>

  <section class="card card-back">
    <div class="back-mark">
      <span class="mark-circle"></span>
      <span class="mark-name">Bramwell Outworks</span>
    </div>
    <p class="back-url">www.bramwelloutworks.example</p>
  </section>

  <section class="card card-front">
    <div class="faint-ring"></div>
    <svg class="front-edges" viewBox="0 0 600 343" aria-hidden="true">
      <polygon points="0,0 18,0 18,258 0,252" fill="#5d6166"/>
      <polygon points="0,252 30,262 78,343 0,343" fill="#1477c4"/>
    </svg>

    <div class="brand-lockup">
      <span class="mark-circle"></span>
      <span class="divider"></span>
      <span class="mark-name">Bramwell<br>Outworks</span>
    </div>
    <div class="top-rule"></div>

    <ul class="services">
      <li>Storm Restoration</li>
      <li>Roofing</li>
      <li>Siding</li>
      <li>Windows</li>
    </ul>

    <div class="person">
      <h1 class="person-name">Dorian Halvek</h1>
      <p class="person-title">Director</p>
    </div>

    <ul class="contacts">
      <li>
        <svg viewBox="0 0 24 24"><path d="M6.6 10.8a15.1 15.1 0 0 0 6.6 6.6l2.2-2.2a1 1 0 0 1 1-.25 11.4 11.4 0 0 0 3.6.57 1 1 0 0 1 1 1V20a1 1 0 0 1-1 1A17 17 0 0 1 3 4a1 1 0 0 1 1-1h3.5a1 1 0 0 1 1 1c0 1.25.2 2.45.57 3.57a1 1 0 0 1-.25 1z"/></svg>
        <span>555-418-7302</span>
      </li>
      <li>
        <svg viewBox="0 0 24 24"><path d="M6 2h12v6H6zM4 9h16a2 2 0 0 1 2 2v6h-4v5H6v-5H2v-6a2 2 0 0 1 2-2zm4 6v5h8v-5z"/></svg>
        <span>555-418-9047</span>
      </li>
      <li>
        <svg viewBox="0 0 24 24"><path d="M2 5h20v14H2zm2 2v.5l8 5 8-5V7zm0 2.8V17h16V9.8l-8 5z"/></svg>
        <span>info@bramwelloutworks.example</span>
      </li>
      <li>
        <svg viewBox="0 0 24 24"><path d="M12 2a10 10 0 1 0 0 20 10 10 0 0 0 0-20zm6.9 6h-3a15 15 0 0 0-1.3-3.9A8 8 0 0 1 18.9 8zM12 4c.8 1.1 1.5 2.5 1.9 4h-3.8c.4-1.5 1.1-2.9 1.9-4zM4.3 14a8 8 0 0 1 0-4h3.4a16 16 0 0 0 0 4zm.8 2h3a15 15 0 0 0 1.3 3.9A8 8 0 0 1 5.1 16zm3-8h-3a8 8 0 0 1 4.3-3.9A15 15 0 0 0 8.1 8zM12 20c-.8-1.1-1.5-2.5-1.9-4h3.8c-.4 1.5-1.1 2.9-1.9 4zm2.3-6H9.7a14 14 0 0 1 0-4h4.6a14 14 0 0 1 0 4zm.3 5.9a15 15 0 0 0 1.3-3.9h3a8 8 0 0 1-4.3 3.9zm1.7-5.9a16 16 0 0 0 0-4h3.4a8 8 0 0 1 0 4z"/></svg>
        <span>www.<span class="url-accent">bramwelloutworks</span>.example</span>
      </li>
    </ul>
  </section>

</body>
</html>
```